Dinner Invitation for an email

Please create an image I can embed in an email. The tone should be sophisticated, fun and festive.

Here is the copy:

FOOD | FRIENDS | FUN
Please join QBR and friends at Corvell's Harbor Room for cocktails, conversation and a delectable dinner
Date: Monday, January 23 (during NPDF)
Time: Cocktails start at 6:30 | Dinner is around 7
Place: Corvell's Harbor Room - The Pearl Terrace
27318 W Bramwick Pkwy - Scottsdale
(Adjacent to the Halloway Brightmere Lodge)

RSVP: nora.whitby@qbrvantage.com
(Nora will send you a calendar invite)

Hope to see you there!

```html
<!DOCTYPE html>
<html lang="en">
<head>
<meta charset="UTF-8">
<title>QBR Dinner Invitation</title>
<link href="https://fonts.googleapis.com/css2?family=Bebas+Neue&family=Montserrat:wght@400;600;700&family=Pinyon+Script&display=swap" rel="stylesheet">
<style>
  :root {
    --page: #e6e6ea;
    --navy-deep: #03033a;
    --navy: #05086b;
    --navy-mid: #0a1290;
    --glow: #2f7bff;
    --white: #ffffff;
    --footer-ink: #1f2a7a;
    --halo: rgba(40, 60, 200, 0.22);
  }
  * { margin: 0; padding: 0; box-sizing: border-box; }
  html, body {
    width: 911px; height: 1200px; overflow: hidden;
    background: var(--page);
  }
  .invitation {
    position: absolute; left: 183px; top: 20px;
    width: 545px; height: 1159px;
    background: linear-gradient(180deg, var(--navy-deep) 0%, #04045a 45%, var(--navy) 100%);
    overflow: hidden;
    font-family: "Montserrat", Arial, sans-serif;
    color: var(--white);
  }
  .edge-glow {
    position: absolute; left: 0; width: 100%; height: 14px;
    background: radial-gradient(ellipse 55% 100% at 50% 50%, #cfe4ff 0%, var(--glow) 30%, rgba(20,40,200,0) 75%);
  }
  .edge-glow--top { top: -6px; }
  .edge-glow--bottom { top: 1059px; }
  .backdrop-circles { position: absolute; left: 0; top: 560px; width: 545px; height: 500px; }
  .brand {
    position: absolute; top: 82px; left: 0; width: 100%;
    display: flex; justify-content: center; align-items: center; gap: 10px;
  }
  .brand__mark { width: 26px; height: 26px; background: var(--navy-mid); border: 0; }
  .brand__name { font-family: "Montserrat", Arial, sans-serif; font-weight: 700; font-size: 34px; color: var(--white); letter-spacing: 1px; }
  .confetti {
    position: absolute; left: 20px; width: 505px;
    background: radial-gradient(ellipse at 50% 50%, rgba(120,80,200,0.28) 0%, rgba(40,60,200,0.12) 55%, rgba(3,3,58,0) 80%);
  }
  .confetti--upper { top: 178px; height: 100px; }
  .confetti--lower { top: 352px; height: 122px; }
  .headline {
    position: absolute; top: 290px; left: 0; width: 100%;
    text-align: center;
    font-family: "Bebas Neue", "Arial Narrow", sans-serif;
    font-size: 56px; line-height: 1; letter-spacing: 0.5px;
    white-space: nowrap;
  }
  .headline span { -webkit-background-clip: text; background-clip: text; color: transparent; }
  .headline__food { background-image: linear-gradient(90deg, #e8441e, #f39a2a); }
  .headline__friends { background-image: linear-gradient(90deg, #f8d84a, #2fc7d8 50%, #7a4ad8 85%, #c94aa0); }
  .headline__fun { background-image: linear-gradient(90deg, #f2c12e, #2ec24a 60%, #129a3c); }
  .headline__divider { background-image: linear-gradient(#f0a021, #f0a021); margin: 0 10px; }
  .welcome {
    position: absolute; top: 508px; left: 90px; width: 365px;
    text-align: center;
    font-family: "Pinyon Script", cursive;
    font-size: 27px; line-height: 48px;
  }
  .detail {
    position: absolute; left: 38px; width: 480px;
    display: flex; align-items: flex-start;
  }
  .detail__icon { flex: none; }
  .detail__text { position: absolute; left: 91px; font-weight: 700; font-size: 14.5px; line-height: 18px; white-space: nowrap; }
  .detail--when { top: 748px; }
  .detail--when .detail__text { top: 0; }
  .detail__time { display: block; margin-top: 17px; }
  .detail--where { top: 871px; }
  .detail--where .detail__text { top: 10px; }
  .rsvp {
    position: absolute; left: 0; top: 1066px; width: 100%; height: 93px;
    background: var(--white);
    color: var(--footer-ink);
    text-align: center;
    font-size: 20px; line-height: 26px; padding-top: 13px;
  }
</style>
</head>
<body>
  <main class="invitation">
    <div class="edge-glow edge-glow--top"></div>

    <svg class="backdrop-circles" viewBox="0 0 545 500" aria-hidden="true">
      <circle cx="210" cy="150" r="140" fill="var(--halo)"/>
      <rect x="272" y="60" width="200" height="140" fill="rgba(40,60,200,0.12)"/>
      <circle cx="272" cy="270" r="200" fill="rgba(40,60,200,0.08)"/>
      <circle cx="370" cy="480" r="130" fill="rgba(40,60,200,0.14)"/>
    </svg>

    <div class="brand">
      <span class="brand__mark"></span>
      <span class="brand__name">QBR</span>
    </div>

    <div class="confetti confetti--upper" role="img" aria-label="Scattered colourful confetti dots and twinkling stars"></div>
    <div class="confetti confetti--lower" role="img" aria-label="Scattered colourful confetti dots with golden sparkles"></div>

    <h1 class="headline">
      <span class="headline__food">Food</span><span class="headline__divider">|</span><span class="headline__friends">Friends</span><span class="headline__divider">|</span><span class="headline__fun">Fun</span>
    </h1>

    <p class="welcome">Please join QBR and friends at Corvell's Harbor Room for cocktails, conversation and a delectable dinner</p>

    <section class="detail detail--when">
      <svg class="detail__icon" width="78" height="78" viewBox="0 0 78 78" aria-hidden="true">
        <rect x="3" y="10" width="58" height="52" rx="5" fill="none" stroke="#fff" stroke-width="5"/>
        <rect x="3" y="10" width="58" height="12" fill="#fff"/>
        <rect x="14" y="2" width="6" height="14" rx="3" fill="#fff"/>
        <rect x="44" y="2" width="6" height="14" rx="3" fill="#fff"/>
        <g fill="#fff">
          <circle cx="16" cy="32" r="4"/><circle cx="29" cy="32" r="4"/><circle cx="42" cy="32" r="4"/>
          <circle cx="16" cy="45" r="4"/><circle cx="29" cy="45" r="4"/>
        </g>
        <circle cx="58" cy="58" r="17" fill="var(--navy)" stroke="#fff" stroke-width="5"/>
        <path d="M58 49 V59 H50" fill="none" stroke="#fff" stroke-width="4" stroke-linecap="round"/>
      </svg>
      <p class="detail__text">Monday, January 23<br>(during NPDF)<span class="detail__time">Cocktails start at 6:30 | Dinner is around 7</span></p>
    </section>

    <section class="detail detail--where">
      <svg class="detail__icon" width="60" height="76" viewBox="0 0 60 76" aria-hidden="true">
        <path d="M30 72 C18 56 4 42 4 28 A26 26 0 0 1 56 28 C56 42 42 56 30 72 Z" fill="none" stroke="#fff" stroke-width="5" stroke-linejoin="round"/>
        <circle cx="30" cy="28" r="7" fill="#fff"/>
      </svg>
      <p class="detail__text">Corvell's Harbor Room - The Pearl Terrace<br>27318 W Bramwick Pkwy - Scottsdale<br>(Adjacent to the Halloway Brightmere Lodge)</p>
    </section>

    <div class="edge-glow edge-glow--bottom"></div>

    <footer class="rsvp">
      <p>RSVP: nora.whitby@qbrvantage.com</p>
      <p>(Nora will send you a calendar invite)</p>
    </footer>
  </main>
</body>
</html>
```